Harborlight Unity Collective Sponsorship

FULL PROJECT DESCRIPTION PROVIDED IN PDF AND WORD DOC (UPLOADED).

Harborlight Unity Collective is looking for an updated sponsorship package design – included in the shared information is our sponsorship packaged used in 2017, 2018, and 2019.

The mission of Harborlight Unity Collective is to create opportunities for integrating and promoting visibility for the lesbian. gay, bisexual and transgender community; promoting equal rights and diversity through public education and the arts; provide safe opportunities and venues for people to come out with the ability to express and celebrate their sexual identities.

Some images (because of their size) are not allowed to be uploaded... use the following link to access the full library of images, reference documents, and the full outline: https://files.vexorabox.net/shared/7qTmW3zK9-4rbLnYcP2sVdHgE6uJaXf0N?mode=view

Sponsorship packet design details:
Final file type: .pdf and/or .ai/.eps
Orientation: Preferably landscape but not opposed to a portrait design.
Page count: estimated 6 with current content (not opposed to 8 pages)
Size: 8.5”x11”
Full bleed

Images:
Images for this design are shared in a folder “images for use in sponsorship packet” – please feel free to choose them as you see fit and we can make any notes after the first draft.

Creative Reference:
Additionally, provided are a few sponsorship packages that we like and feel that you might be able to take inspiration from – these are in a folder named “sponsorship packets we like”
Updates

I've updated all of the details of this project and would like to have completed asap. Thank you.

Target Market(s)

Primarily our target market is local and regional businesses that are interested in supporting GlowFair through sponsorship or might be interested in advertising opportunities.

Industry/Entity Type

LGBT

Font styles to use
Serif
Sans Serif

Colors

Designer to choose colors to be used in the design.

Requirements
Must have
• All sponsorship details

```html
<!DOCTYPE html>
<html lang="en">
<head>
<meta charset="utf-8">
<title>Harborlight Unity Collective – Sponsorship Packages</title>
<link rel="stylesheet" href="https://fonts.googleapis.com/css2?family=Oswald:wght@400;500;700&family=Roboto:wght@400;700&family=Roboto+Slab:wght@400;700&family=Passion+One&display=swap">
<style>
:root{
  --bg:#e4e4e4;
  --paper:#ffffff;
  --ink:#2b2b2b;
  --muted:#555;
  --orange:#e8893a;
  --red:#dd4a2a;
  --crimson:#b7292c;
  --purple:#5b3d8f;
  --violet:#7d3c98;
  --green:#6fb23c;
  --lime:#8cc63f;
  --yellow:#e2d524;
  --blue:#3f73b8;
  --teal:#5fbfa3;
  --mint:#cdeadd;
  --navy:#2d3a5a;
  --slab:"Roboto Slab", Georgia, serif;
  --sans:"Roboto", Arial, sans-serif;
  --cond:"Oswald", "Arial Narrow", sans-serif;
}
*{box-sizing:border-box;margin:0;padding:0}
html,body{width:1200px;height:2348px;overflow:hidden;background:var(--bg)}
body{position:relative;font-family:var(--sans);color:var(--ink)}
.spread{position:absolute;left:180px;width:840px;height:570px;display:flex;box-shadow:0 6px 18px rgba(0,0,0,.18)}
.spread--one{top:110px}.spread--two{top:890px}.spread--three{top:1670px}
.page{position:relative;width:420px;height:570px;background:var(--paper);overflow:hidden}
.abs{position:absolute}
.photo{position:absolute}
.brand{font-family:var(--cond);font-weight:700;color:var(--navy);text-transform:uppercase;line-height:1;display:flex;align-items:center;gap:5px}
.brand .mark{width:12px;height:12px;background:currentColor;flex:none}
p,li{font-size:6px;line-height:1.45}
/* spread one */
.details{left:160px;top:40px;width:250px}
.details h2{font-family:var(--sans);font-size:14px;line-height:1.2;font-weight:400;color:var(--red)}
.details h2 b{color:var(--purple)}
.details ul{margin-top:36px;padding-left:12px}
.details li{margin-bottom:8px}
.band-orange{background:var(--orange)}
.section-title{font-family:var(--cond);font-weight:500;font-size:10px;color:var(--red);text-transform:uppercase}
table.fees{width:100%;border-collapse:collapse;font-size:5.5px}
table.fees th{font-weight:700;padding:2px 2px;text-align:center}
table.fees td{padding:3px 2px;text-align:center}
table.fees tr.shade td{background:var(--mint)}
table.fees td.lbl{text-align:right;padding-right:6px}
.note{font-size:6px;color:var(--muted)}
/* spread two sponsorship */
.title-band{background:var(--lime);left:0;top:42px;width:420px;height:62px}
.title-band h1{position:absolute;left:136px;top:8px;font-family:"Passion One", Impact, sans-serif;font-weight:400;font-size:18px;line-height:.95;color:var(--purple);text-transform:uppercase}
.title-band .sub{position:absolute;left:136px;top:46px;font-family:var(--sans);font-weight:700;font-size:7px;color:#222}
.intro{left:22px;top:112px;width:385px;font-family:var(--slab);font-size:5.6px;line-height:1.45;color:#444}
.levels-bar{left:0;top:175px;width:420px;height:14px;background:var(--yellow);text-align:center;font-family:var(--cond);font-weight:500;font-size:9px;line-height:14px;color:var(--purple);text-transform:uppercase}
.tier{position:absolute;left:0;width:420px;display:flex;padding:6px 14px 0 22px;font-family:var(--slab)}
.tier h3{font-family:var(--cond);font-weight:400;font-size:9px;color:#333;text-transform:uppercase;margin-bottom:2px}
.tier .col{width:50%}
.tier .col p{font-size:4.6px;line-height:1.4;color:#444}
.tier .col.right{padding-top:8px}
/* spread three */
.carte{position:absolute;left:0;width:420px;overflow:hidden}
.carte h4{font-family:var(--cond);font-weight:400;font-size:15px;text-transform:uppercase;line-height:1}
.carte p{font-family:var(--slab);font-size:4.8px;line-height:1.45}
.carte em{font-style:italic;font-weight:700}
.cover-title{left:68px;top:378px;width:290px;height:80px;border:2px solid #bbb;text-align:center;padding-top:10px}
.cover-title .l1{font-family:var(--sans);font-size:16px;color:var(--lime);letter-spacing:.5px}
.cover-title .l2{font-family:var(--sans);font-weight:700;font-size:15px;color:var(--lime);letter-spacing:4px}
.cover-title .l3{font-family:var(--sans);font-weight:700;font-size:8px;color:#333;letter-spacing:5px;margin-top:5px}
.contact{display:flex;align-items:center;gap:4px;font-size:5.5px;color:#fff;font-weight:700}
</style>
</head>
<body>

<!-- Spread one: sponsorship details and vendor registration -->
<section class="spread spread--one">
  <div class="page">
    <div class="photo" role="img" aria-label="Festival-goers posing in rainbow costumes at the fair" style="left:0;top:0;width:160px;height:355px;background:linear-gradient(160deg,#c8b9a0,#7e6f8a 55%,#3f4a5a)"></div>
    <div class="abs details">
      <h2>SPONSORSHIP DETAILS<br><b>&amp; DEADLINES</b></h2>
      <ul>
        <li>Sponsorship agreements must be completed by <b>Saturday, June 1, 2019.</b><br><b>*Please Note:</b> Sponsors receiving advertising related benefits must have their agreement completed and be paid in full no later than May 1, 2019 for guaranteed inclusion in applicable advertising – per sponsorship benefit.*<br><br>Please make checks payable to <b>Harborlight Unity Collective</b> and send to <b>PO Box 4410 Harbor City, ST 00410.</b></li>
        <li>Logos in PDF or EPS format should be sent to <u>ads@harborlightunity.org</u> as soon as possible, but no later than <b>Wednesday, May 1, 2019.</b></li>
        <li>Final print ready artwork for included Harborlight Guide ads should be sent to <u>ads@harborlightunity.org</u> as soon as possible, but no later than Wednesday, May 1, 2019.<br><i>Additional information for advertising benefits available in the guide ad specs 2019.</i></li>
        <li>Completed vendor/parade registration for included sponsors – completed no later than <b>Saturday, June 1, 2019.</b></li>
      </ul>
    </div>
    <div class="photo" role="img" aria-label="Crowd with colourful balloons behind a parade banner" style="left:0;top:360px;width:300px;height:210px;background:linear-gradient(180deg,#9fc7d9,#c05a7c 45%,#2e2c3a)"></div>
    <div class="photo" role="img" aria-label="Fairground ride against the sky" style="left:306px;top:366px;width:114px;height:204px;background:linear-gradient(150deg,#d9e8f2,#e8c46a 60%,#b07a4b)"></div>
  </div>
  <div class="page">
    <div class="abs band-orange" style="left:0;top:18px;width:240px;height:62px"></div>
    <div class="abs" style="left:30px;top:32px;font-size:8px;line-height:1.1;color:#5a3a1e;font-weight:700">Development<br>Committee Meeting<br><span style="font-weight:400;font-size:5.5px">Approved and in effect 11/28/2018</span></div>
    <div class="abs brand" style="left:250px;top:34px;width:120px;font-size:11px;flex-wrap:nowrap"><span class="mark"></span><span>Harborlight Unity<br>Collective</span></div>
    <div class="abs band-orange" style="left:385px;top:18px;width:35px;height:62px"></div>
    <div class="abs section-title" style="left:30px;top:95px">Vendor Registration Details</div>
    <p class="abs" style="left:30px;top:120px">Registration deadlines have been approved as follows:</p>
    <div class="abs" style="left:30px;top:132px;width:365px">
      <table class="fees">
        <tr><th></th><th>Food Vendors</th><th>General Vendors</th><th>Nonprofit Vendors</th></tr>
        <tr class="shade"><td class="lbl">Pre-registration <b>1/15/19</b></td><td>$300</td><td>$250</td><td>$125</td></tr>
        <tr><td class="lbl">Regular <b>5/15/2019</b></td><td>$350</td><td>$300</td><td>$175</td></tr>
        <tr class="shade"><td class="lbl">Late <b>6/1/2019</b></td><td>$450</td><td>$400</td><td>$275</td></tr>
      </table>
      <table class="fees" style="margin-top:6px">
        <tr><th>Sales Permit</th><th>Chairs</th><th>Tables</th><th>Tents</th></tr>
        <tr class="shade"><td>$15</td><td>$5</td><td>$10</td><td>$195</td></tr>
      </table>
      <p class="note" style="margin-top:4px"><i>for each group the difference between early and regular registration is $50.</i></p>
      <p class="note">a waitlist will be started on 5/15/2019, registrations received after that date must be approved to participate.<br>Waitlisted vendors will receive notification no later than 6/1/2019 if space is available.</p>
      <p class="note" style="margin-top:3px">Generator Safety</p>
    </div>
    <div class="abs" style="left:0;top:360px;width:420px;height:200px;background:var(--teal)"></div>
    <div class="abs" style="left:352px;top:268px;width:14px;height:88px;background:var(--red)"></div>
    <div class="abs" style="left:25px;top:292px;width:372px;height:240px;background:#fff;padding:4px">
      <div class="photo" role="img" aria-label="Performer on stage before a large festival crowd" style="position:relative;width:100%;height:100%;background:linear-gradient(180deg,#a9b7c6,#9a5a45 40%,#8b3a4a 70%,#3c2c38)"></div>
    </div>
  </div>
</section>

<!-- Spread two: parade registration and sponsorship levels -->
<section class="spread spread--two">
  <div class="page">
    <div class="photo" role="img" aria-label="Dancers performing on the main stage with city skyline behind" style="left:0;top:0;width:420px;height:200px;background:linear-gradient(180deg,#c5ccd3,#8d7d80 45%,#5a4f63 75%,#70757c)"></div>
    <div class="abs section-title" style="left:38px;top:222px">Parade Registration Details</div>
    <p class="abs" style="left:38px;top:237px">Registration deadlines have been approved as follows:</p>
    <div class="abs" style="left:38px;top:250px;width:362px">
      <table class="fees">
        <tr><th></th><th colspan="3">Nonprofit</th><th colspan="4">General</th></tr>
        <tr><th></th><th>Walking</th><th>Cars*</th><th>Trucks</th><th>Walking</th><th>Cars*</th><th>Tracks</th><th>Motor</th></tr>
        <tr class="shade"><td class="lbl">Pre-registration <b>1/15/19</b></td><td>$60</td><td>$100</td><td>$120</td><td>$120</td><td>$140</td><td>$200</td><td>$35</td></tr>
        <tr><td class="lbl">Regular <b>5/15/2019</b></td><td>$90</td><td>$130</td><td>$150</td><td>$150</td><td>$170</td><td>$230</td><td>$70</td></tr>
      </table>
      <p class="note" style="margin-top:8px"><i>for each group the difference between early and regular registration is $30.</i></p>
      <p class="note" style="margin-top:3px">a waitlist will be started on 5/15/2019, registrations received after that date must be approved to participate.<br>Waitlisted parade contingents will receive notification no later than 6/1/2019 if space is available.</p>
      <p class="note" style="margin-top:4px">Minor alterations in pricing were made to accommodate for billing structure.</p>
      <p class="note" style="margin-top:4px"><b>Registration payment deadline</b>(s) for pre-registration must be post marked for 1/15/2019, all registrations received will be subject to the "regular" price increase. Registrations must be paid for in full by June 1, 2019 – registrations unpaid are subject to forfeit their registration due to non-payment.</p>
    </div>
    <div class="photo" role="img" aria-label="Performer in blue wig on stage beside brick building" style="left:0;top:420px;width:218px;height:150px;background:linear-gradient(160deg,#9c5a44,#6d6b8f 60%,#3a3340)"></div>
    <div class="photo" role="img" aria-label="Crowd gathered in front of a stone building" style="left:232px;top:420px;width:188px;height:150px;background:linear-gradient(180deg,#b5b2a9,#6e6770 55%,#3b3a44)"></div>
  </div>
  <div class="page">
    <div class="photo" role="img" aria-label="Rainbow flags waving above a parade crowd" style="left:0;top:0;width:420px;height:42px;background:linear-gradient(90deg,#7a5a60,#c0853e,#5c8fa8,#7c4e6e)"></div>
    <div class="abs title-band">
      <div class="abs brand" style="left:18px;top:18px;font-size:9px;width:110px"><span class="mark"></span><span>Harborlight Unity<br>Collective</span></div>
      <h1>Harborlight GlowFair &amp;<br>Illuminated Night Parade</h1>
      <div class="sub">2019 SPONSORSHIP &amp; MARKETING OPPORTUNITIES</div>
    </div>
    <p class="abs intro">Harborlight's GlowFair &amp; Illuminated Night Parade has become one of the largest events in the City of Harbor City and one of the largest LGBTQ Pride events in the Northeast. This past years events drew over 85,000 (estimated by the Harbor City Emergency Management Office). With this amazing growth of our events we have also increased the opportunity for businesses and organizations to be a part of our community. We invite you to review the various opportunities and benefits available. We are also able to customize a sponsorship package based on your area of interest.</p>
    <div class="abs levels-bar">Sponsorship Levels &amp; Benefits</div>

    <div class="tier" style="top:189px;height:92px;background:#e7ebf2">
      <div class="col"><h3>Presenting - $20,000+</h3><p>- First choice ad placement in the official Harborlight Guide (Back cover, inside front, back cover or inside page)<br>- 10 x 20 first choice, booth space at GlowFair<br>- First choice placement in Illuminated Night Parade<br>- Ten VIP Access Passes: Brightwater Garden &amp; Entertainer Meet and Greet (as available)</p></div>
      <div class="col right"><p>- Name/Logo Banner placements at GlowFair &amp; Parade<br>- Name/Logo on Promotional Advertising<br>- Name/Logo on all sponsor acknowledgement media<br>- Opportunity for ad placement on harborlightunity.org homepage<br>- Use of the annual theme and Harborlight Logo<br>- Special recognition at Harborlight Honors Gala</p></div>
    </div>
    <div class="tier" style="top:281px;height:57px;background:#cfd0d2">
      <div class="col"><h3>Platinum - $10,000+</h3><p>- One full page ad in the official Harborlight Guide*<br>- 10 x 20 premium booth space at GlowFair<br>- Premium placement in Illuminated Night Parade</p></div>
      <div class="col"><p>- Six VIP Access Passes: Brightwater Garden &amp; Entertainer Meet and Greet<br>- Name/Logo on Promotional Advertising<br>- Name/Logo on all sponsor acknowledgement media<br>- Opportunity for ad placement on harborlightunity.org homepage<br>- Use of the annual theme and Harborlight Logo</p></div>
    </div>
    <div class="tier" style="top:338px;height:55px;background:#f4f2d3">
      <div class="col"><h3>Gold - $7,000+</h3><p>- One half-page ad placement in the official Harborlight Guide*<br>- 10 x 20 premium booth space at GlowFair<br>- Premium Placement in Illuminated Night Parade</p></div>
      <div class="col"><p>- Four VIP Access Passes: Brightwater Garden &amp; Entertainer Meet &amp; Greets<br>- Name/Logo on Promotional Advertising<br>- Name/Logo on all sponsor acknowledgement media<br>- Opportunity for ad placement on harborlightunity.org homepage<br>- Use of the annual theme and Harborlight Logo</p></div>
    </div>
    <div class="tier" style="top:393px;height:45px;background:#e3e4e8">
      <div class="col"><h3>Silver - $5,000+</h3><p>- One quarter-page ad placement in the official Harborlight Guide*<br>- 10 x 10 booth space at GlowFair</p></div>
      <div class="col"><p>- Placement in Illuminated Night Parade<br>- Two VIP Access Passes: Brightwater Garden &amp; Entertainer Meet &amp; Greets<br>- Name/Logo on all sponsor acknowledgement media<br>- Use of the annual theme and Harborlight Logo</p></div>
    </div>
    <div class="tier" style="top:438px;height:42px;background:#f5e6da">
      <div class="col"><h3>Bronze - $3,000+</h3><p>- One eighth-page ad placement in the official Harborlight Guide*<br>- 10 x 10 booth space at GlowFair</p></div>
      <div class="col"><p>- Placement in Illuminated Night Parade<br>- Name/Logo on all sponsor acknowledgement media<br>- Use of the annual theme and Harborlight Logo</p></div>
    </div>
    <div class="tier" style="top:480px;height:42px;background:#e6dcee">
      <div class="col"><h3>Lavender - $1,500+</h3><p>- 10 x 10 booth space at GlowFair<br>- Placement in the Illuminated Night Parade</p></div>
      <div class="col right"><p>- Name/logo on all sponsor acknowledgement media<br>- Use of the annual theme and Harborlight Logo</p></div>
    </div>
    <div class="abs" style="left:0;top:522px;width:200px;height:48px;background:#e8efe0"></div>
    <p class="abs" style="left:22px;top:532px;font-family:var(--slab);font-size:4.8px;color:#555">Mailing Address: PO Box 4410 Harbor City, ST 00410<br>Office: 208 Lantern Row, Harbor City, ST 00412<br>T: 555-467-0193 &nbsp;|&nbsp; harborlightunity.org</p>
    <div class="photo" role="img" aria-label="Cover of the printed visitors guide" style="left:205px;top:522px;width:36px;height:44px;background:linear-gradient(150deg,#2b2b3a,#9c3f8e 50%,#e2a63a);transform:rotate(-4deg)"></div>
    <p class="abs" style="left:252px;top:530px;width:160px;font-family:var(--slab);font-size:4.8px;color:#555">*The official Harborlight Visitors Guide is printed in full color with more than 8,500 copies distributed throughout the region, nearby states and cities.</p>
  </div>
</section>

<!-- Spread three: back cover a la carte and front cover -->
<section class="spread spread--three">
  <div class="page">
    <div class="carte" style="top:0;height:85px;background:var(--orange);color:#fff">
      <h4 style="position:absolute;left:22px;top:14px;font-size:26px;font-weight:500">A La Carte Options</h4>
      <p style="position:absolute;left:22px;top:50px;font-size:9px;font-weight:700;line-height:1.2">Harborlight GlowFair &amp; Illuminated Night<br>Parade Sponsorship Opportunities</p>
      <div class="photo" role="img" aria-label="Crowd in front of a stone building" style="left:262px;top:0;width:158px;height:55px;background:linear-gradient(180deg,#9a9994,#56505c)"></div>
    </div>
    <div class="carte" style="top:55px;height:120px;background:transparent">
      <svg class="abs" width="420" height="120" style="left:0;top:0"><polygon points="170,30 420,0 420,120 190,120" fill="var(--green)"/></svg>
      <div class="photo" role="img" aria-label="Festival tents on a sunny day" style="left:0;top:30px;width:180px;height:70px;background:linear-gradient(180deg,#a9c4d9,#5f6a58 60%,#3f4d3c)"></div>
      <div class="abs" style="right:14px;top:8px;text-align:right;color:#fff;width:230px">
        <h4>General</h4>
        <p><em>Downtown Rainbow Banner Trail: $9,500</em><br>40 pole banners · 20 banners including sponsor's logo</p>
        <p style="margin-top:3px"><em>Harborlight Homepage / Newsletter Advertising:</em><br>$250/week (May-June) · $150/week (March-April) · $50/week (July-Feb)</p>
        <p style="margin-top:3px"><em>VIP &amp; Volunteer Appreciation Party Sponsor: $2,500</em></p>
      </div>
    </div>
    <div class="carte" style="top:162px;height:95px;background:var(--yellow);color:#222">
      <div class="photo" role="img" aria-label="Performers in bright costumes" style="left:280px;top:0;width:140px;height:95px;background:linear-gradient(160deg,#5a4c6e,#b4723f 60%,#3a3a50)"></div>
      <div class="abs" style="left:22px;top:8px;width:250px">
        <h4>GlowFair</h4>
        <p><em>Gateway Banners: $750 each (four available)</em></p>
        <p style="margin-top:3px"><em>KidsZone: $2,500</em><br>Two barricade banners · 10 x 10 booth placement · Main stage recognition</p>
        <p style="margin-top:3px"><em>Volunteer T-Shirts: $3,000</em><br>Logo placement on back of volunteer shirts</p>
      </div>
    </div>
    <div class="carte" style="top:257px;height:82px;background:var(--blue);color:#fff">
      <div class="photo" role="img" aria-label="Night parade with lit storefronts" style="left:0;top:0;width:105px;height:82px;background:linear-gradient(160deg,#5a2a1e,#c9873a 45%,#2a2030)"></div>
      <div class="abs" style="right:14px;top:6px;text-align:right;width:290px">
        <h4>Parade</h4>
        <p><em>Barricade Banners placed along parade route:</em> $250 each or three for $600</p>
        <p style="margin-top:4px"><em>Reviewing Stand Sponsorship:</em> $5,000<br>Up to four barricade banners · Ad/logo placement<br>Four · 20-second promotional "shout-out" by emcee</p>
      </div>
    </div>
    <div class="carte" style="top:339px;height:110px;background:var(--violet);color:#fff">
      <div class="photo" role="img" aria-label="Main stage with large screen and audience" style="left:280px;top:0;width:140px;height:75px;background:linear-gradient(180deg,#3a4a7a,#6f8fbf 50%,#2a2a38)"></div>
      <div class="abs" style="left:22px;top:8px;width:270px">
        <h4>Entertainment / Main Stage</h4>
        <p><em>Headline Sponsor: $25,000</em><br>Prime placement of up to eight barricade banners and one digital ad on stage</p>
        <p style="margin-top:4px"><em>Five-Second Static Ad on Stage LED Board: $300 each</em></p>
        <p style="margin-top:4px"><em>Thirty-Second Commercial on Stage LED Board: $1,000 each</em></p>
        <p style="margin-top:4px"><em>Hospitality / Information Station: $2,000+</em><br>Brand recognition and signage at station</p>
      </div>
    </div>
    <div class="carte" style="top:449px;height:121px;background:var(--crimson);color:#fff">
      <div class="photo" role="img" aria-label="Friends smiling at the garden party" style="left:0;top:0;width:120px;height:121px;background:linear-gradient(160deg,#7a4a3a,#d4a27a 50%,#5a2a2a)"></div>
      <div class="abs" style="right:14px;top:6px;text-align:right;width:290px">
        <h4>Beer, Wine &amp; Spirits Garden</h4>
        <p><em>Beer Sponsor: $5,000+</em><br>Unlimited branding (within available space) · Countdown to Pride promotional opportunities</p>
        <p style="margin-top:3px"><em>Spirits Sponsor: $5,000+</em><br>Limited branding (within available space) · Countdown to Pride promotional opportunities</p>
        <p style="margin-top:3px"><em>Wine Sponsors: $5,000+</em><br>Limited branding (within available space) · Countdown to Pride promotional opportunities</p>
        <p style="margin-top:3px"><em>Water Bottle Sponsorship: $3,500+</em><br>Branded water bottles. (Quantity TBD)</p>
      </div>
    </div>
  </div>
  <div class="page">
    <div class="abs" style="left:160px;top:0;width:260px;height:90px;background:var(--red)"></div>
    <div class="abs brand" style="left:18px;top:24px;font-size:12px;width:140px"><span class="mark" style="width:16px;height:16px"></span><span>Harborlight Unity<br>Collective</span></div>
    <div class="abs contact" style="left:172px;top:38px">
      <svg width="8" height="8" viewBox="0 0 8 8"><circle cx="4" cy="4" r="3.5" fill="none" stroke="#fff" stroke-width=".8"/><path d="M2.3 3h3.4v2.2H2.3z M2.3 3l1.7 1.2L5.7 3" fill="none" stroke="#fff" stroke-width=".5"/></svg>ads@harborlightunity.org
    </div>
    <div class="abs contact" style="left:255px;top:38px">
      <svg width="8" height="8" viewBox="0 0 8 8"><circle cx="4" cy="4" r="3.5" fill="none" stroke="#fff" stroke-width=".8"/><rect x="3" y="2" width="2" height="4" rx=".4" fill="none" stroke="#fff" stroke-width=".5"/></svg>555-206-0148
    </div>
    <div class="abs contact" style="left:318px;top:34px;line-height:1.2">
      <svg width="8" height="10" viewBox="0 0 8 10"><path d="M4 9.5C1.5 6 1 5 1 3.7a3 3 0 0 1 6 0C7 5 6.5 6 4 9.5z" fill="none" stroke="#fff" stroke-width=".8"/><circle cx="4" cy="3.7" r="1" fill="#fff"/></svg><span>P.O. Box 4410,<br>Harbor City, ST 00410</span>
    </div>
    <div class="abs" style="left:395px;top:90px;width:25px;height:370px;background:var(--red)"></div>
    <div class="photo" role="img" aria-label="Aerial view of festival tents by the river with city skyline" style="left:0;top:90px;width:395px;height:225px;background:linear-gradient(180deg,#c9d3dc,#8a9aa5 35%,#6f8a5a 65%,#9aa86a)"></div>
    <div class="abs" style="left:250px;top:272px;width:145px;height:58px;background:var(--purple);color:#fff;font-family:var(--cond);font-weight:500;font-size:28px;text-align:center;line-height:58px">JUNE 2019</div>
    <div class="abs cover-title">
      <div class="l1">HARBORLIGHT GLOWFAIR</div>
      <div class="l2">AND NIGHT PARADE</div>
      <div class="l3">SPONSORSHIP PACKAGES</div>
    </div>
    <div class="abs" style="left:160px;top:460px;width:260px;height:110px;background:var(--red)"></div>
    <div class="photo" role="img" aria-label="Festival tents with rainbow umbrella" style="left:0;top:472px;width:80px;height:98px;background:linear-gradient(180deg,#b8c7d6,#c9725a 60%,#5a6a4a)"></div>
    <div class="photo" role="img" aria-label="Large rainbow flag" style="left:82px;top:472px;width:115px;height:98px;background:linear-gradient(160deg,#e23b3b,#f19a2c 25%,#f2d43a 45%,#4aa85a 65%,#3a6fc0 82%,#7a3e9a)"></div>
    <div class="photo" role="img" aria-label="Crowd with balloons behind a parade banner" style="left:199px;top:472px;width:90px;height:98px;background:linear-gradient(180deg,#9fc7d9,#c05a7c 50%,#2e2c3a)"></div>
    <div class="photo" role="img" aria-label="Two festival title holders wearing sashes" style="left:291px;top:472px;width:129px;height:98px;background:linear-gradient(160deg,#8a9aa8,#b88a7a 50%,#4a3a4a)"></div>
  </div>
</section>

</body>
</html>
```